Verostel business card

Business card for sustainable investment company called "Verostel". Verostel is an exchange platform selling carbon credits between buyers and sellers. Carbon Credits are an environmental commodity for reducing global carbon emissions.

the card should obviously have our logo and the theme should be sustainability/environment mixed with a trading platform.

Contact Information for Business Card

Logo, Name, Title, Phone, Email

Colors
0054AA
0677BA
7BADD7
CADEEF
E8F1F8
0094D4
00A9DD
6FCCEA
C7EBF8
E9F6FB
00AB8E
00BBA5
67D7C9
C6EFE9
E9F9F6
59FF00
82FF00
B8FF75
E3FFCB
F4FFEA

```html
<!DOCTYPE html>
<html lang="en">
<head>
<meta charset="utf-8">
<title>Verostel Business Card</title>
<link href="https://fonts.googleapis.com/css2?family=Figtree:wght@400;500;700;800&display=swap" rel="stylesheet">
<style>
  :root {
    --backdrop: #ebebe9;
    --navy-dark: #1a2943;
    --navy: #24375a;
    --navy-light: #2c4166;
    --ink: #17233a;
    --card-white: #f2f2f1;
    --teal: #4fb6c6;
    --blue: #2f6fb8;
    --white: #ffffff;
  }
  * { box-sizing: border-box; margin: 0; padding: 0; }
  html, body {
    width: 1200px; height: 1200px; overflow: hidden;
    background: var(--backdrop);
    font-family: "Figtree", sans-serif;
    color: var(--ink);
  }
  .card {
    position: absolute;
    left: 234px;
    width: 732px;
    height: 418px;
    box-shadow: 0 14px 30px rgba(0,0,0,0.12);
  }
  .card-front { top: 160px; }
  .card-back { top: 632px; background: var(--card-white); }

  .front-pattern {
    position: absolute; inset: 0;
    background: linear-gradient(100deg, var(--navy-dark) 0%, var(--navy) 50%, var(--navy-light) 100%);
  }
  .front-brand {
    position: absolute; left: 0; right: 0; top: 0; bottom: 0;
    display: flex; align-items: center; justify-content: center; gap: 18px;
  }
  .brand-square {
    width: 34px; height: 34px; background: var(--white);
  }
  .front-brand .brand-name {
    font-weight: 700; font-size: 40px; letter-spacing: 1px; color: var(--white);
  }

  .rule {
    position: absolute; left: 67px; width: 596px; height: 2px; background: var(--ink);
  }
  .rule-top { top: 62px; }
  .rule-bottom { top: 174px; }

  .person-name {
    position: absolute; left: 67px; top: 86px;
    font-size: 33px; font-weight: 700;
    background: linear-gradient(90deg, var(--teal), var(--blue));
    -webkit-background-clip: text; background-clip: text; color: transparent;
  }
  .person-title {
    position: absolute; left: 67px; top: 127px;
    font-size: 20px; font-weight: 400;
  }
  .office-name {
    position: absolute; left: 67px; top: 212px;
    font-size: 19px; font-weight: 800;
  }
  .office-address {
    position: absolute; left: 67px; top: 238px;
    font-size: 20px; font-weight: 400;
  }
  .contact-list {
    position: absolute; left: 67px; top: 274px;
    list-style: none;
  }
  .contact-list li {
    display: flex; align-items: center; gap: 8px;
    font-size: 20px; height: 27.5px;
  }
  .contact-list svg { width: 15px; height: 15px; }

  .back-brand {
    position: absolute; right: 67px; top: 302px;
    display: flex; align-items: center; gap: 14px;
  }
  .back-brand .brand-square { width: 30px; height: 30px; background: var(--ink); }
  .back-brand .brand-name {
    font-weight: 700; font-size: 36px; letter-spacing: 0.5px; color: var(--ink);
  }
</style>
</head>
<body>
  <section class="card card-front">
    <div class="front-pattern" role="img" aria-label="Navy background with a repeating embossed brand-mark pattern"></div>
    <div class="front-brand">
      <span class="brand-square"></span>
      <span class="brand-name">VEROSTEL</span>
    </div>
  </section>

  <section class="card card-back">
    <div class="rule rule-top"></div>
    <h1 class="person-name">Mark Halmos</h1>
    <p class="person-title">Sales Representative</p>
    <div class="rule rule-bottom"></div>

    <p class="office-name">Verostel Head Office</p>
    <p class="office-address">Budapest XIII. Kisfalu utca 14.</p>

    <ul class="contact-list">
      <li>
        <svg viewBox="0 0 16 16" aria-hidden="true"><path d="M4 1.5l2.2 3-1.3 1.6a8 8 0 0 0 5 5l1.6-1.3 3 2.2-1.3 2.4C8 14 2 8 1.6 2.8z" fill="var(--blue)"/></svg>
        +36 30 555 0142
      </li>
      <li>
        <svg viewBox="0 0 16 16" aria-hidden="true"><rect x="1" y="3" width="14" height="10" fill="var(--blue)"/><path d="M1 3l7 6 7-6" stroke="#fff" stroke-width="1.2" fill="none"/></svg>
        szerviz@verostel.com
      </li>
      <li>
        <svg viewBox="0 0 16 16" aria-hidden="true"><circle cx="8" cy="8" r="6.5" fill="none" stroke="var(--blue)" stroke-width="1.5"/><ellipse cx="8" cy="8" rx="2.8" ry="6.5" fill="none" stroke="var(--blue)" stroke-width="1.2"/><path d="M1.5 8h13" stroke="var(--blue)" stroke-width="1.2"/></svg>
        www.verostel.com
      </li>
    </ul>

    <div class="back-brand">
      <span class="brand-square"></span>
      <span class="brand-name">VEROSTEL</span>
    </div>
  </section>
</body>
</html>
```